Business Card - high end, modern health care

Hey designers!

We need a double sided business card for the boutique, cutting edge physical therapy rehabilitation centre in Sydney's Northern Beaches.

With the most qualified physios in the area The Harbourline Motion Clinic does what other physiotherapy practices do not, we take our time with our patients giving them longer appointments, better physios and therefor faster results!

We guarantee that the service people receive at THMC will be unparalleled.

Hence we need a business card to reflect our modern, boutique, high end service. The final design needs to reflect that we are in a class of our own yet with the feel of beachside retreat.

Below I have attached our logo in both blue on white and white on blue. The exact colour is;
and the font that we have used in our logo is Tex Gyre Aventador.

I like the idea of the blue as the main colour as it is more eye catching and our signage onto the main road will be in this blue and in the interest of consistency across marketing the blue needs to be a part of the design. However I would appreciate a few designs onto a wooden background as this is a visual theme within the fitout of the practice.

The design needs to be of standard size (91x55mm).

Target Market(s)

We target people who have an end outcome in mind and those who have had poor experiences with other providers and ensure that everyone gets the care that they deserve with a premium service that is tailored to the individuals circumstances. As a premium service, the target market is highly educated, business and tech savvy with the additional target market of elderly people who have self funded their retirement and see value in paying for the best ongoing rehabilitation to maintain independence.

Industry/Entity Type

Physical Therapy

Contact Information for Business Card

Name, designation( Titled Musculoskeletal Physiotherapist... there will also be those in the company that have multiple designations ie 5 or 6 words long), phone number, email, facebook, instagram, address

Font styles to use
Sans Serif

Colors

Designer to choose colors to be used in the design.

Requirements
Must have
• Front - The logo as large as possible, blue or wooden theme, and all of the important details.
• Back - A blank space/lines on which to write appointment times (no "Appointment, date, time" etc.)
Nice to have
• facebook url
• logos for facebook and instagram
• Mini logos for the phone and email?

```html
<!DOCTYPE html>
<html lang="en">
<head>
<meta charset="utf-8">
<title>The Harbourline Motion Clinic – Business Card</title>
<link rel="stylesheet" href="https://fonts.googleapis.com/css2?family=Montserrat:wght@400;500;600;700&display=swap">
<style>
  :root {
    --brand-blue: #1f5fae;
    --brand-blue-deep: #123f85;
    --brand-blue-light: #2a78c2;
    --paper: #f4f4f2;
    --stage: #e6e7e9;
    --ink-white: #ffffff;
  }
  * { box-sizing: border-box; margin: 0; padding: 0; }
  html, body {
    width: 1200px; height: 900px; overflow: hidden;
    background: var(--stage);
    font-family: "Montserrat", sans-serif;
  }
  .canvas {
    width: 1200px; height: 900px;
    display: flex; align-items: center; justify-content: center; gap: 70px;
  }
  .card {
    width: 460px; height: 760px;
    border-radius: 28px;
    position: relative;
    display: flex; flex-direction: column; align-items: center;
    box-shadow: 0 10px 30px rgba(0,0,0,0.12);
  }
  .card--front {
    background: radial-gradient(circle at 60% 55%, var(--brand-blue-light) 0%, var(--brand-blue) 45%, var(--brand-blue-deep) 100%);
    color: var(--ink-white);
    padding-top: 62px;
  }
  .card--back {
    background: var(--paper);
    color: var(--brand-blue);
    padding-top: 88px;
  }
  .holder-name { font-weight: 700; font-size: 25px; letter-spacing: 1px; }
  .holder-title { font-size: 16px; font-weight: 400; margin-top: 4px; }
  .dash { width: 26px; height: 2px; background: currentColor; margin: 24px 0; }
  .brand-mark {
    width: 240px; height: 240px; border-radius: 50%;
    border: 3px solid currentColor;
  }
  .brand-name {
    font-weight: 600; font-size: 24px; letter-spacing: 1.5px;
    text-transform: uppercase; text-align: center; line-height: 1.25;
    margin-top: 30px;
  }
  .address { font-size: 20px; font-weight: 600; text-align: center; line-height: 1.5; margin-top: 28px; }
  .icon-row { display: flex; gap: 22px; margin-top: 28px; }
  .icon { width: 30px; height: 30px; }
  .contact { font-size: 18px; font-weight: 500; text-align: center; line-height: 1.9; margin-top: 26px; }
  .card--front .dash--end { margin-top: 16px; }
  .appointment-lines { display: flex; flex-direction: column; gap: 14px; margin-top: 46px; width: 330px; }
  .appointment-line { height: 56px; border: 2px solid var(--brand-blue); border-radius: 14px; }
  .card--back .dash--end { margin-top: 30px; }
</style>
</head>
<body>
<main class="canvas">
  <section class="card card--front" aria-label="Card front">
    <p class="holder-name">DANIEL ASHWORTH</p>
    <p class="holder-title">Titled Musculoskeletal Physiotherapist</p>
    <span class="dash"></span>
    <div class="brand-mark"></div>
    <p class="brand-name">The Harbourline<br>Motion Clinic</p>
    <p class="address">1247 Calder Lane<br>VIC 3000 Australia</p>
    <div class="icon-row">
      <svg class="icon" viewBox="0 0 30 30" aria-label="Phone">
        <circle cx="15" cy="15" r="13" fill="none" stroke="#fff" stroke-width="2"/>
        <path d="M10 9.5c1-1 2-1 2.6 0l1 1.8c.4.7.2 1.3-.4 1.8l-.6.5c.6 1.5 1.8 2.7 3.3 3.3l.5-.6c.5-.6 1.1-.8 1.8-.4l1.8 1c1 .6 1 1.6 0 2.6-1.5 1.5-4 .9-6.6-1.7S8.5 11 10 9.5z" fill="#fff"/>
      </svg>
      <svg class="icon" viewBox="0 0 30 30" aria-label="Email">
        <circle cx="15" cy="15" r="13" fill="none" stroke="#fff" stroke-width="2"/>
        <rect x="8.5" y="10.5" width="13" height="9" rx="1" fill="none" stroke="#fff" stroke-width="1.6"/>
        <path d="M8.8 11l6.2 5 6.2-5" fill="none" stroke="#fff" stroke-width="1.6"/>
      </svg>
      <svg class="icon" viewBox="0 0 30 30" aria-label="Social profile one">
        <circle cx="15" cy="15" r="13" fill="none" stroke="#fff" stroke-width="2"/>
      </svg>
      <svg class="icon" viewBox="0 0 30 30" aria-label="Social profile two">
        <circle cx="15" cy="15" r="13" fill="none" stroke="#fff" stroke-width="2"/>
      </svg>
    </div>
    <p class="contact">0061 482 310<br>contact@harbourlinemotion.com.au<br>harbourlinemotionclinic</p>
    <span class="dash dash--end"></span>
  </section>

  <section class="card card--back" aria-label="Card back">
    <div class="brand-mark"></div>
    <p class="brand-name">The Harbourline<br>Motion Clinic</p>
    <div class="appointment-lines">
      <div class="appointment-line"></div>
      <div class="appointment-line"></div>
      <div class="appointment-line"></div>
    </div>
    <span class="dash dash--end"></span>
  </section>
</main>
</body>
</html>
```